Optical Finish Trainer (OFT)

I would like to design a dedicated site for my OFT product, which allows industry employees to be trained in the visual inspection of mechanical parts. My product is a 3D simulator (see https://brenko-atel.example/our-applications/virtual-reality/ and https://brenko-atel.example for videos) which makes it possible to manufacture standard parts representative of a type of defect which is accepted or refused by the quality department. These master parts can be used to create a common quality culture in the company and to train employees in a homogeneous way. The simulator is initially designed for watchmaking, but must be designed for much broader industries (cars, phone reconditioning, ball bearings, etc.)
L'information que j'ai donnée n'est pas assez précise. Je dois préciser les domaines métiers visés par le site internet. J'ai besoin de quelques jours pour choisir les domaines les plus représentatifs.

```html
<!DOCTYPE html>
<html lang="en">
<head>
<meta charset="utf-8">
<title>Optical Finish Trainer</title>
<link href="https://fonts.googleapis.com/css2?family=Poppins:wght@300;400;500;600;700&display=swap" rel="stylesheet">
<style>
:root{
  --teal:#0b8198;
  --teal-dark:#0d5f70;
  --deep:#0f4f5f;
  --footer:#0e3c49;
  --ink:#1e1e1e;
  --text:#4a4a4a;
  --rule:#b9b9b9;
  --bottom:#262626;
}
*{margin:0;padding:0;box-sizing:border-box}
html,body{width:1200px;height:4286px;overflow:hidden}
body{font-family:'Poppins',sans-serif;color:var(--text);position:relative;background:#fff}
.abs{position:absolute}
section,header,footer{position:absolute;left:0;width:1200px}
/* top bar */
.topbar{top:0;height:37px;background:var(--teal);color:#fff;font-size:11px}
.topbar .right{position:absolute;right:0;top:0;width:460px;height:37px;background:var(--teal-dark);clip-path:polygon(28px 0,100% 0,100% 100%,0 100%)}
.topbar .item{position:absolute;top:11px;display:flex;align-items:center;gap:6px}
.icon-dot{width:22px;height:22px;border-radius:50%;background:var(--deep);display:inline-flex;align-items:center;justify-content:center}
/* nav */
.nav{top:37px;height:89px;background:#fff;box-shadow:0 2px 6px rgba(0,0,0,.06)}
.brand{position:absolute;left:111px;top:18px;color:var(--teal);font-weight:700;font-size:22px;line-height:26px}
.brand small{display:block;color:var(--ink);font-weight:500;font-size:15px;letter-spacing:14px}
.nav a{position:absolute;top:32px;font-size:14px;color:#555;text-decoration:none}
.nav a.active{color:var(--teal)}
.nav a.active::after{content:"";position:absolute;left:0;top:26px;width:44px;height:3px;background:var(--teal)}
.btn{display:inline-flex;align-items:center;gap:12px;border-radius:24px;font-weight:600;font-size:13px;text-decoration:none}
.btn .arr{width:18px;height:18px;border-radius:50%;display:inline-flex;align-items:center;justify-content:center}
.btn-teal{background:var(--teal-dark);color:#fff;padding:0 14px 0 22px;height:43px}
.btn-teal .arr{background:#fff}
.btn-white{background:#fff;color:var(--teal);padding:0 14px 0 20px;height:42px}
.btn-white .arr{background:var(--teal)}
/* hero */
.hero{top:126px;height:576px;background:linear-gradient(100deg,#1c7d8e 0%,#2a8a9a 45%,#4d4d4d 58%,#777 80%,#3a3a3a 100%)}
.hero .photo{position:absolute;inset:0;clip-path:polygon(62% 0,100% 0,100% 100%,42% 100%);background:radial-gradient(circle at 72% 30%,#bbb 0,#7a7a7a 30%,#333 75%)}
.hero h1{position:absolute;left:111px;top:115px;color:#fff;font-size:42px;font-weight:700;line-height:52px}
.hero p{position:absolute;left:111px;top:222px;color:#fff;font-size:19px;line-height:30px;font-weight:500}
.slide-arrow{position:absolute;top:224px;width:58px;height:58px;border-radius:50%;border:1.5px solid rgba(255,255,255,.8);display:flex;align-items:center;justify-content:center}
/* headings */
.h2{font-size:38px;font-weight:700;color:var(--ink);line-height:45px}
.h2 span{color:var(--teal)}
.rule{position:absolute;height:2px;background:var(--rule)}
.rule::after{content:"";position:absolute;left:50%;top:-2px;width:16px;height:5px;margin-left:-8px;background:var(--teal-dark)}
.rule.left::after{left:92px}
.list{list-style:none;font-size:14.5px;line-height:25px}
.list li{position:relative;padding-left:30px;text-align:justify}
.list li::before{content:"›";position:absolute;left:0;top:4px;width:15px;height:15px;border:1.2px solid var(--teal);border-radius:50%;color:var(--teal);font-size:12px;line-height:12px;text-align:center}
.body-p{font-size:14.5px;line-height:25px;text-align:justify}
/* control */
.control{top:702px;height:646px}
/* lighten */
.lighten{top:1348px;height:532px;background:linear-gradient(90deg,#f2f2f2 0%,#ececec 45%,#d8d8d8 65%,#9c9c9c 100%)}
/* quote */
.quote{top:1880px;height:270px;background:#2b7f90}
.quote p{position:absolute;left:168px;top:68px;width:897px;color:#fff;font-size:20.5px;line-height:32px;text-align:justify;text-align-last:center}
/* allows */
.allows{top:2150px;height:599px}
/* awareness */
.aware{top:2749px;height:539px}
/* cards */
.cards{top:3288px;height:576px;background:var(--deep)}
.card{position:absolute;color:#fff;overflow:hidden}
.card h3{font-size:23px;font-weight:600}
.card a{color:#fff;font-size:12px;font-weight:600}
.card p{font-size:12.5px;line-height:21px;margin:6px 0}
/* footer */
.foot{top:3864px;height:353px;background:var(--footer);color:#fff}
.vline{position:absolute;top:0;width:1px;height:353px;background:rgba(255,255,255,.25)}
.foot h4{position:absolute;top:115px;font-size:16px;font-weight:600;padding-left:20px;border-left:4px solid #1aa3c0}
.foot h4::after{content:"";position:absolute;left:20px;top:32px;width:40px;height:2px;background:#1aa3c0}
.foot ul{position:absolute;top:166px;list-style:none;font-size:12px;line-height:26px;font-weight:500}
.contact-row{position:absolute;left:140px;display:flex;gap:18px;font-size:12.5px;line-height:18px}
.contact-row .ic{width:34px;height:34px;border-radius:50%;background:#1e5968;display:flex;align-items:center;justify-content:center;flex:none}
.contact-row small{font-size:11px;color:#bcd}
.copy{top:4217px;height:69px;background:var(--bottom);color:#ddd;font-size:13px;text-align:center;line-height:69px}
.totop{position:absolute;right:45px;top:-9px;width:38px;height:38px;background:var(--teal);border-radius:4px;display:flex;align-items:center;justify-content:center}
</style>
</head>
<body>

<header class="topbar">
  <div class="item" style="left:111px"><span class="icon-dot"><svg width="11" height="9" viewBox="0 0 11 9"><rect x=".5" y=".5" width="10" height="8" fill="none" stroke="#fff"/><path d="M.5 .5l5 4 5-4" fill="none" stroke="#fff"/></svg></span> Email: <b>m.dorval@brenko-atel.example</b> &nbsp;&nbsp;|&nbsp;&nbsp; <b>l.keller@quartzline.example</b></div>
  <div class="item" style="left:623px"><span style="width:22px;height:22px;border-radius:50%;background:#e8e8e8;display:inline-block"></span> English ▾</div>
  <div class="right">
    <div class="item" style="left:44px"><span class="icon-dot"><svg width="11" height="11" viewBox="0 0 24 24"><path fill="#fff" d="M6.6 10.8a15 15 0 006.6 6.6l2.2-2.2a1 1 0 011-.25 11 11 0 003.6.6 1 1 0 011 1V20a1 1 0 01-1 1A17 17 0 013 4a1 1 0 011-1h3.5a1 1 0 011 1c0 1.25.2 2.45.6 3.6a1 1 0 01-.25 1z"/></svg></span> Call or Text : <b>+41 70 555 01 24</b> &nbsp;|&nbsp; <b>+41 70 555 08 67</b></div>
  </div>
</header>

<header class="nav">
  <div class="brand">OPTICAL FINISH<small>TRAINER</small></div>
  <a class="active" href="#" style="left:404px">Home</a>
  <a href="#" style="left:484px">In regards to</a>
  <a href="#" style="left:610px">Services</a>
  <a href="#" style="left:705px">Partners</a>
  <a href="#" style="left:800px">References</a>
  <a href="#" style="left:915px">Info</a>
  <a class="btn btn-teal" href="#" style="left:963px;top:21px;color:#fff;height:43px;background:var(--teal)">Contact Us <span class="arr"><svg width="8" height="8" viewBox="0 0 8 8"><path d="M2 1l3 3-3 3" stroke="#0b8198" stroke-width="1.6" fill="none"/></svg></span></a>
</header>

<section class="hero">
  <div class="photo" role="img" aria-label="Watchmaker's hand adjusting a mechanical watch movement with tweezers"></div>
  <h1>OPTICAL FINISH<br>TRAINER</h1>
  <p>VIRTUAL REALITY AT THE SERVICE OF<br>CONTROLLED AESTHETIC WATCHMAKING</p>
  <a class="btn btn-white abs" href="#" style="left:108px;top:309px">Contact Us <span class="arr"><svg width="8" height="8" viewBox="0 0 8 8"><path d="M2 1l3 3-3 3" stroke="#fff" stroke-width="1.6" fill="none"/></svg></span></a>
  <div class="slide-arrow" style="left:24px"><svg width="18" height="12" viewBox="0 0 18 12"><path d="M17 6H2M6 1L1 6l5 5" stroke="#fff" stroke-width="1.6" fill="none"/></svg></div>
  <div class="slide-arrow" style="left:1115px;border-color:rgba(255,255,255,.5)"><svg width="18" height="12" viewBox="0 0 18 12"><path d="M1 6h15M12 1l5 5-5 5" stroke="#fff" stroke-width="1.6" fill="none"/></svg></div>
</section>

<section class="control">
  <h2 class="h2 abs" style="left:0;width:1200px;text-align:center;top:80px">AESTHETIC CONTROL: <span>HOW TO CONTROL IT?</span></h2>
  <div class="rule" style="left:503px;top:130px;width:197px"></div>
  <div class="abs" style="left:111px;top:363px;width:209px;height:220px;background:var(--deep)"></div>
  <div class="abs" role="img" aria-label="Team of colleagues reviewing documents around a table in a bright office" style="left:143px;top:156px;width:434px;height:404px;background:linear-gradient(135deg,#c9a27c,#8a6a4e 45%,#d9d2c6)"></div>
  <ul class="list abs" style="left:625px;top:164px;width:432px">
    <li style="margin-bottom:18px">Adopting a simple and unambiguous language for a common understanding of aesthetic quality at the extended enterprise level.</li>
    <li style="margin-bottom:18px">By using a semantic reference matrix associating the types of anomalies (scratches, marks, deformations, stains, etc.) with the intensity levels defined with the company.</li>
    <li style="margin-bottom:18px">Determining the compliance thresholds of the component or product.</li>
    <li>Providing uniform training in operational competence for those responsible for aesthetic control.</li>
  </ul>
  <a class="btn btn-teal abs" href="#" style="left:625px;top:518px;background:var(--teal-dark)">Learn More <span class="arr"><svg width="8" height="8" viewBox="0 0 8 8"><path d="M2 1l3 3-3 3" stroke="#0d5f70" stroke-width="1.6" fill="none"/></svg></span></a>
</section>

<section class="lighten">
  <div class="abs" role="img" aria-label="Business team meeting around a conference table seen from above" style="left:560px;top:0;width:640px;height:532px;background:linear-gradient(120deg,rgba(240,240,240,0) 0%,#b9b6b0 30%,#7a6d60 60%,#c8c8c8 100%)"></div>
  <h2 class="h2 abs" style="left:109px;top:78px">LIGHTEN THE MANAGEMENT <span>OF</span><br><span>PHYSICAL COMPONENTS</span></h2>
  <div class="rule left" style="left:109px;top:183px;width:196px"></div>
  <p class="body-p abs" style="left:109px;top:208px;width:402px">Companies must manage and maintain sets of physical components used as a "yardstick" for the training of aesthetic testers.</p>
  <p class="body-p abs" style="left:109px;top:300px;width:402px">The cost of managing a set of physical parts representing all combinations of shapes, defect types, materials and finishes is very high.</p>
  <a class="btn btn-teal abs" href="#" style="left:110px;top:405px;background:var(--teal-dark)">Learn More <span class="arr"><svg width="8" height="8" viewBox="0 0 8 8"><path d="M2 1l3 3-3 3" stroke="#0d5f70" stroke-width="1.6" fill="none"/></svg></span></a>
</section>

<section class="quote">
  <p>"In the implementation of the new Qualiticiennes en microtechnique course, the Lakeside School of Watchmaking has deployed the OFT application to teach the methods of aesthetic control. This application fully meets the pedagogical objectives as well as the ease of use by both our teaching staff and our students."</p>
</section>

<section class="allows">
  <div class="abs" role="img" aria-label="Close-up of an open pocket watch movement being repaired with tweezers" style="left:0;top:0;width:563px;height:599px;background:radial-gradient(circle at 45% 55%,#d9b27a 0,#8a6232 35%,#3b2a1a 80%)"></div>
  <h2 class="h2 abs" style="left:624px;top:76px">OFT <span>ALLOWS</span> :</h2>
  <div class="rule" style="left:624px;top:127px;width:196px"></div>
  <ul class="list abs" style="left:624px;top:155px;width:432px">
    <li style="margin-bottom:14px">Remove the management of components used as standards for aesthetic control training</li>
    <li style="margin-bottom:14px">To make employees aware of aesthetic control and the vocabulary to be used</li>
    <li style="margin-bottom:14px">Integrate aesthetic control into a total quality management (TQM) approach with precise indicators at all stages of the manufacturing and after-sales processes</li>
    <li>Provide the after-sales service with an efficient tool to record the aesthetic aspect of the supported product</li>
  </ul>
  <a class="btn btn-teal abs" href="#" style="left:624px;top:471px;background:var(--teal-dark)">Learn More <span class="arr"><svg width="8" height="8" viewBox="0 0 8 8"><path d="M2 1l3 3-3 3" stroke="#0d5f70" stroke-width="1.6" fill="none"/></svg></span></a>
</section>

<section class="aware">
  <h2 class="h2 abs" style="left:111px;top:70px">RAISING AWARENESS OF CRITERIA <span>&amp;</span><br><span>AESTHETIC VOCABULARY</span></h2>
  <div class="rule left" style="left:111px;top:174px;width:196px"></div>
  <p class="body-p abs" style="left:111px;top:200px;width:517px">Aesthetic defects are often the result of careless handling of the components and products concerned, whether during manufacture, assembly or marketing.</p>
  <p class="body-p abs" style="left:111px;top:291px;width:517px">By making the OFT platform available to staff in direct contact with the product, it becomes very easy to make them aware of the evaluation criteria and the aesthetic vocabulary defined by the company.</p>
  <a class="btn btn-teal abs" href="#" style="left:110px;top:406px;background:var(--teal-dark)">Learn More <span class="arr"><svg width="8" height="8" viewBox="0 0 8 8"><path d="M2 1l3 3-3 3" stroke="#0d5f70" stroke-width="1.6" fill="none"/></svg></span></a>
  <svg class="abs" style="left:670px;top:120px" width="405" height="380" viewBox="0 0 405 380">
    <path d="M205 6 A185 185 0 0 1 160 372" fill="none" stroke="#1a8aa2" stroke-width="8"/>
  </svg>
  <div class="abs" role="img" aria-label="Cheerful group of coworkers celebrating together" style="left:685px;top:135px;width:355px;height:355px;border-radius:50%;background:radial-gradient(circle at 45% 40%,#f1ece6 0,#c9c2ba 55%,#8f8a86 100%)"></div>
</section>

<section class="cards">
  <div class="card" role="img" aria-label="Hand holding tweezers over a watch movement" style="left:115px;top:87px;width:470px;height:403px;background:linear-gradient(180deg,#c9bfb2 0%,#7a6f63 45%,#1f1c1a 85%)">
    <div class="abs" style="left:13px;top:252px;width:440px">
      <h3>Improve after-sales service returns</h3>
      <p>The OFT platform can easily be used by the service network staff to assist them in the objective assessment of aesthetic defects by referring to the semantic matrix as well as to the cases already referenced.</p>
      <a href="#">Learn More</a>
    </div>
  </div>
  <div class="card" role="img" aria-label="Crowd of business people gathered at an event" style="left:617px;top:87px;width:470px;height:187px;background:linear-gradient(180deg,#d8d4ce 0%,#7d746a 50%,#1e1b19 100%)">
    <div class="abs" style="left:24px;top:105px"><h3>Improving the total quality approach</h3><a href="#">Learn More</a></div>
  </div>
  <div class="card" role="img" aria-label="Employees working at desks in an open-plan office" style="left:617px;top:304px;width:470px;height:186px;background:linear-gradient(180deg,#e4e8ea 0%,#8a8a88 50%,#1e1c1b 100%)">
    <div class="abs" style="left:24px;top:104px"><h3>A semantic matrix of aesthetic defects</h3><a href="#">Learn More</a></div>
  </div>
</section>

<footer class="foot">
  <div class="vline" style="left:117px"></div>
  <div class="vline" style="left:493px"></div>
  <div class="vline" style="left:770px"></div>
  <div class="vline" style="left:971px"></div>
  <h4 style="left:117px">CONTACT US</h4>
  <div class="contact-row" style="top:170px"><span class="ic"><svg width="12" height="15" viewBox="0 0 12 15"><path d="M6 0a6 6 0 016 6c0 4-6 9-6 9S0 10 0 6a6 6 0 016-6z" fill="#1aa3c0"/><circle cx="6" cy="6" r="2" fill="#1e5968"/></svg></span><div><small>Address</small><br>42 Linden Row, Halvern<br>Toronto, Canada, 00000</div></div>
  <div class="contact-row" style="top:238px"><span class="ic"><svg width="14" height="14" viewBox="0 0 24 24"><path fill="#1aa3c0" d="M6.6 10.8a15 15 0 006.6 6.6l2.2-2.2a1 1 0 011-.25 11 11 0 003.6.6 1 1 0 011 1V20a1 1 0 01-1 1A17 17 0 013 4a1 1 0 011-1h3.5a1 1 0 011 1c0 1.25.2 2.45.6 3.6a1 1 0 01-.25 1z"/></svg></span><div><small>Call Us</small><br>+41 70 555 01 24, +41 70 555 08 67</div></div>
  <div class="contact-row" style="top:292px"><span class="ic"><svg width="14" height="11" viewBox="0 0 14 11"><rect width="14" height="11" rx="1" fill="#1aa3c0"/><path d="M0 1l7 5 7-5" stroke="#1e5968" fill="none"/></svg></span><div><small>Email</small><br>m.dorval@brenko-atel.example<br>l.keller@quartzline.example</div></div>
  <h4 style="left:493px">QUICK LINKS</h4>
  <ul style="left:516px"><li>HOME</li><li>IN REGARDS TO</li><li>SERVICES</li><li>PARTNERS</li><li>REFERENCES</li><li>INFO</li></ul>
  <h4 style="left:770px">LINKS</h4>
  <ul style="left:794px"><li>COPYRIGHT</li><li>LEGAL</li><li>PRIVACY</li><li>ACCESSIBILITY</li><li>SITEMAP</li></ul>
  <h4 style="left:971px">SUPPORT</h4>
  <ul style="left:998px"><li>TEAM</li><li>ABOUT US</li><li>CAREERS</li><li>OUR VALUES</li></ul>
</footer>

<footer class="copy">
  ©2023. All rights reserved.
  <div class="totop"><svg width="12" height="8" viewBox="0 0 12 8"><path d="M1 7l5-5 5 5" stroke="#fff" stroke-width="1.8" fill="none"/></svg></div>
</footer>

</body>
</html>
```